Banner for promote service of debit card

We are PagaVelo and we need the banners to be posted on the facebook and instagram pages.
We want something to communicate that it is an exclusive debit card full of services.
Low commissions.
Our competitors:
https://www.nortapay-pagos.it/it/home.html
https://www.zelkor-conti.it/it/
https://www.fotoreelz.it/serravanbank/
sendquillo
maybe some banner that makes the idea of a convenient debit card that everyone can use.
Girls enjoying card shopping.
Please check also website for slogans and phrases to use
https://www.pagavelo-carta.it/
Should show the services.
We must convey that it is a fast, simple card that guarantees privacy.
We need strong banners that attract people as these ban will be sponsored on instagram and facebook
Target Market(s)
People 18-35 y
Open Bank account. low commissions. Easy to use. No limits. 100% Privacy.
Requirements
Must have
- Written in Italian.

```html
<!DOCTYPE html>
<html lang="it">
<head>
<meta charset="utf-8">
<title>PagaVelo – Una carta per tutti</title>
<link rel="stylesheet" href="https://fonts.googleapis.com/css2?family=Montserrat:wght@400;600;700;800;900&display=swap">
<style>
  :root {
    --ink: #1f1f1f;
    --muted: #4a4a4a;
    --magenta: #d2146c;
    --amber: #fbb417;
    --white: #ffffff;
    --brand-grey: #6d6d6d;
    --brand-accent: #f2603a;
  }
  * { margin: 0; padding: 0; box-sizing: border-box; }
  html, body { width: 1200px; height: 628px; overflow: hidden; background: var(--white); }
  .banner {
    position: relative; width: 1200px; height: 628px; overflow: hidden;
    background: var(--white); font-family: "Montserrat", sans-serif; color: var(--ink);
  }
  .photo {
    position: absolute; left: 560px; top: 0; width: 640px; height: 500px;
    background:
      radial-gradient(ellipse 220px 260px at 330px 170px, #8a4a34 0%, #a46a52 45%, rgba(230,220,215,0) 100%),
      linear-gradient(90deg, rgba(255,255,255,1) 0%, #eef0f2 30%, #e6e8ea 100%);
  }
  .deco { position: absolute; inset: 0; }
  .card-fan {
    position: absolute; left: 450px; top: 378px; width: 470px; height: 180px;
    border-radius: 16px;
    background: linear-gradient(100deg, #e9566a 0%, #d98ea8 30%, #1d8fd0 55%, #25b98a 80%, #3fd3b0 100%);
    transform: rotate(-8deg);
  }
  .card-held {
    position: absolute; left: 948px; top: 292px; width: 186px; height: 120px;
    border-radius: 12px;
    background: linear-gradient(110deg, #d9a3b8 0%, #e9566a 60%, #d8324a 100%);
    transform: rotate(-16deg);
  }
  .headline { position: absolute; left: 85px; top: 76px; font-weight: 900; font-size: 52px; line-height: 1.18; letter-spacing: -0.5px; }
  .headline .accent { color: var(--magenta); display: block; }
  .tagline { position: absolute; left: 85px; top: 203px; font-size: 18px; color: var(--muted); }
  .services { position: absolute; left: 122px; top: 268px; list-style: none; }
  .services li { position: relative; font-weight: 700; font-size: 22.5px; line-height: 31.5px; padding-left: 30px; }
  .services li::before {
    content: ""; position: absolute; left: 0; top: 9px; width: 14px; height: 14px;
    border: 3px solid var(--magenta); border-radius: 50%;
  }
  .contacts { position: absolute; left: 82px; top: 505px; color: var(--white); font-weight: 700; font-size: 20px; }
  .contacts .row { display: flex; align-items: center; gap: 12px; height: 36px; margin-bottom: 12px; }
  .contacts .icon { width: 34px; height: 34px; border-radius: 50%; background: var(--white); display: flex; align-items: center; justify-content: center; }
  .brand { position: absolute; left: 972px; top: 490px; width: 200px; display: flex; flex-direction: column; align-items: center; gap: 12px; }
  .brand .mark { width: 52px; height: 52px; border-radius: 50%; background: var(--brand-accent); }
  .brand .name { font-weight: 800; font-size: 27px; color: var(--brand-grey); }
</style>
</head>
<body>
<main class="banner">
  <div class="photo" role="img" aria-label="Ragazza sorridente che porge una carta di debito"></div>

  <svg class="deco" width="1200" height="628" viewBox="0 0 1200 628" aria-hidden="true">
    <polygon points="0,432 740,585 740,628 0,628" fill="var(--magenta)"/>
    <polygon points="400,628 700,560 870,540 960,628" fill="var(--amber)"/>
  </svg>

  <div class="card-fan" role="img" aria-label="Ventaglio di carte di debito colorate: rosa, blu e verde"></div>
  <div class="card-held" role="img" aria-label="Carta di debito rosa tenuta in mano"></div>

  <h1 class="headline">TUTTO IN UNO!<span class="accent">UNA CARTA PER TUTTI</span></h1>
  <p class="tagline">Usalo come vuoi senza essere controllato</p>

  <ul class="services">
    <li>Apri un conto bancario.</li>
    <li>commissioni basse.</li>
    <li>Facile da usare.</li>
    <li>Senza limiti.</li>
    <li>Privacy al 100%.</li>
  </ul>

  <div class="contacts">
    <div class="row">
      <span class="icon">
        <svg width="18" height="18" viewBox="0 0 24 24" aria-hidden="true"><path fill="var(--magenta)" d="M6.6 10.8a15.1 15.1 0 0 0 6.6 6.6l2.2-2.2c.3-.3.7-.4 1-.2 1.1.4 2.3.6 3.6.6.6 0 1 .4 1 1V20c0 .6-.4 1-1 1A17 17 0 0 1 3 4c0-.6.4-1 1-1h3.5c.6 0 1 .4 1 1 0 1.3.2 2.5.6 3.6.1.3 0 .7-.2 1z"/></svg>
      </span>
      <span class="phone">800-246-1357</span>
    </div>
    <div class="row">
      <span class="icon">
        <svg width="18" height="18" viewBox="0 0 24 24" aria-hidden="true"><g fill="none" stroke="var(--magenta)" stroke-width="2.6" stroke-linecap="round"><path d="M10 14a4 4 0 0 0 5.7 0l3-3a4 4 0 0 0-5.7-5.7l-1 1"/><path d="M14 10a4 4 0 0 0-5.7 0l-3 3a4 4 0 0 0 5.7 5.7l1-1"/></g></svg>
      </span>
      <span class="web">www.pagavelo-carta.it</span>
    </div>
  </div>

  <div class="brand">
    <span class="mark" aria-hidden="true"></span>
    <span class="name">PagaVelo</span>
  </div>
</main>
</body>
</html>
```